Stationery Design for Stone Ridge Septic Systems & Excavating
Business Cards, Envelopes, Letterheads
Stationery Design for Stone Ridge Septic Systems & Excavating - Construction
Creative Brief
Professional
Mark Vandersloot
P.O Box 214 Harrowfield, On N8H 5K2
stoneridgesepticworks@mailbrook.net

```html
<!DOCTYPE html>
<html lang="en">
<head>
<meta charset="utf-8">
<title>Stone Ridge Septic Systems &amp; Excavating – Business Card</title>
<link href="https://fonts.googleapis.com/css2?family=Open+Sans:wght@400;600;700&display=swap" rel="stylesheet">
<style>
  :root {
    --backdrop: #5a5a5a;
    --card-white: #ffffff;
    --brand-blue: #1a4fb0;
    --deep-blue: #0b2f86;
    --bright-blue: #2f6fd8;
    --brand-green: #6cbf1f;
    --text-dark: #3b3b3b;
    --rule-grey: #c9c9c9;
  }
  * { margin: 0; padding: 0; box-sizing: border-box; }
  html, body { width: 1200px; height: 751px; overflow: hidden; }
  body {
    background: var(--backdrop);
    font-family: "Open Sans", Arial, sans-serif;
    position: relative;
  }
  .card {
    position: absolute;
    top: 216px;
    width: 492px;
    height: 283px;
    overflow: hidden;
  }

  /* Front */
  .card-front { left: 91px; background: var(--card-white); }
  .front-brand {
    position: absolute; top: 40px; right: 26px;
    display: flex; align-items: center; gap: 8px;
  }
  .brand-dot { width: 30px; height: 30px; border-radius: 50%; background: var(--brand-blue); }
  .brand-name {
    font-weight: 700; font-size: 22px; color: var(--brand-blue);
    text-transform: uppercase; letter-spacing: 1px; line-height: 1;
  }
  .front-tagline {
    position: absolute; top: 80px; right: 26px;
    font-size: 8px; font-weight: 600; color: var(--brand-green);
    text-transform: uppercase; letter-spacing: 0.5px;
  }
  .person-name {
    position: absolute; left: 24px; top: 146px;
    font-size: 16px; font-weight: 600; color: var(--brand-blue);
    text-transform: uppercase; letter-spacing: 0.3px;
  }
  .name-rule {
    position: absolute; left: 24px; top: 173px; width: 444px; height: 1px;
    background: var(--rule-grey);
  }
  .contact-list {
    position: absolute; left: 24px; top: 186px; list-style: none;
    font-size: 10px; color: var(--text-dark);
  }
  .contact-list li { display: flex; align-items: center; gap: 10px; height: 20px; }
  .contact-list svg { width: 11px; height: 13px; fill: var(--brand-blue); }
  .mailing-address {
    position: absolute; right: 24px; top: 186px; text-align: right;
    font-size: 10px; line-height: 20px; color: var(--text-dark); font-style: normal;
  }
  .front-band {
    position: absolute; left: 0; bottom: 12px; width: 100%; height: 24px;
    display: flex;
  }
  .band-green { width: 60px; background: linear-gradient(90deg, var(--brand-green), #9ad33c); }
  .band-blue {
    flex: 1; background: linear-gradient(90deg, var(--deep-blue), var(--bright-blue) 60%, var(--deep-blue));
    color: #fff; font-size: 10px; letter-spacing: 1px;
    display: flex; align-items: center; justify-content: center;
  }

  /* Back */
  .card-back {
    left: 619px;
    background: radial-gradient(ellipse at 55% 45%, var(--bright-blue), var(--deep-blue) 75%);
  }
  .back-strip {
    position: absolute; left: 0; top: 0; width: 40px; height: 100%;
    background: linear-gradient(180deg, #8fd13a, var(--brand-green));
  }
  .back-brand {
    position: absolute; left: 226px; width: 230px; top: 190px; text-align: center; color: #fff;
  }
  .back-brand .brand-name { color: #fff; font-size: 24px; }
  .back-tagline {
    font-size: 10px; font-weight: 600; text-transform: uppercase; letter-spacing: 0.8px;
    margin-top: 3px;
  }
  .back-web { font-size: 10px; letter-spacing: 0.8px; margin-top: 2px; }
</style>
</head>
<body>

<section class="card card-front" aria-label="Business card front">
  <div class="front-brand">
    <span class="brand-dot"></span>
    <span class="brand-name">Stone Ridge</span>
  </div>
  <div class="front-tagline">Septic Systems &amp; Excavating</div>

  <h1 class="person-name">Mark Vandersloot</h1>
  <div class="name-rule"></div>

  <ul class="contact-list">
    <li>
      <svg viewBox="0 0 11 13" aria-hidden="true"><rect x="1" y="0" width="9" height="13" rx="1.5"/><rect x="2.5" y="1.8" width="6" height="8" fill="#fff"/></svg>
      519-555-0148
    </li>
    <li>
      <svg viewBox="0 0 11 13" aria-hidden="true"><rect x="0" y="3" width="11" height="7.5" rx="1"/><path d="M0.5 3.5 L5.5 7.5 L10.5 3.5" stroke="#fff" stroke-width="1" fill="none"/></svg>
      stoneridgesepticworks@mailbrook.net
    </li>
  </ul>

  <address class="mailing-address">
    P.O Box 214<br>Harrowfield, On N8H 5K2
  </address>

  <div class="front-band">
    <div class="band-green"></div>
    <div class="band-blue">www.stoneridgesepticsystems.com</div>
  </div>
</section>

<section class="card card-back" aria-label="Business card back">
  <div class="back-strip"></div>
  <div class="back-brand">
    <div class="brand-name">Stone Ridge</div>
    <div class="back-tagline">Septic Systems &amp; Excavating</div>
    <div class="back-web">www.stoneridgesepticsystems.com</div>
  </div>
</section>

</body>
</html>
```